Advertisement Sign

Hello,
We're in need of a new design for an advertisement sign. Below is our current concept, but we're looking for improvements. Specifically, we'd like to enhance the size of the 'Call for Assistance' text, possibly explore different fonts, and possibly add a background to make the design more engaging and less plain. We need something that sticks out more. Any suggestions are welcome.

Target Market(s)

Construction and Landscape Companies

```html
<!DOCTYPE html>
<html lang="en">
<head>
<meta charset="utf-8">
<title>Prairie Ridge – Heavy Duty Equipment Rentals Sign</title>
<link rel="stylesheet" href="https://fonts.googleapis.com/css2?family=Michroma&family=Barlow+Condensed:ital,wght@1,700;1,800&family=Exo+2:ital,wght@1,700;1,800&display=swap">
<style>
  :root {
    --page-bg: #e3cdb6;
    --brand-blue: #1f7fd8;
    --sky-deep: #1a5fae;
    --sky-light: #4a90d6;
    --ink: #0d0d0d;
    --white: #ffffff;
    --silver: #cfd6de;
    --flag-red: #d8121b;
    --accent-yellow: #f5c000;
  }
  * { margin: 0; padding: 0; box-sizing: border-box; }
  html, body { width: 1200px; height: 1152px; overflow: hidden; background: var(--page-bg); }
  .sign {
    position: absolute; left: 40px; top: 318px; width: 1120px; height: 515px;
    overflow: hidden; box-shadow: 0 10px 28px rgba(0,0,0,.28);
    font-family: "Michroma", sans-serif; color: var(--ink);
  }
  .sign-shapes { position: absolute; inset: 0; width: 100%; height: 100%; }
  .brand { position: absolute; left: 50px; top: 48px; display: flex; align-items: center; gap: 14px; }
  .brand-square { width: 46px; height: 46px; background: var(--brand-blue); }
  .brand-name { font-family: "Michroma", sans-serif; font-size: 26px; color: var(--ink); letter-spacing: .5px; }
  .headline {
    position: absolute; left: 46px; top: 136px; font-size: 43px; line-height: 44px;
    -webkit-text-stroke: 1.3px var(--ink); letter-spacing: -.5px;
  }
  .region { position: absolute; left: 48px; top: 282px; height: 40px; width: 370px; display: flex; }
  .region span {
    display: flex; align-items: center; justify-content: center; height: 100%;
    color: var(--white); font-size: 19px; letter-spacing: 4px; -webkit-text-stroke: .5px var(--white);
  }
  .region-west { width: 200px; }
  .region-canada { flex: 1; }
  .service {
    position: absolute; left: 50px; top: 344px; font-family: "Barlow Condensed", sans-serif;
    font-style: italic; font-weight: 800; font-size: 29px; color: var(--ink); white-space: nowrap;
  }
  .service em { font-style: italic; color: var(--brand-blue); }
  .slogan {
    position: absolute; left: 760px; top: 40px; width: 322px; text-align: right;
    font-family: "Exo 2", sans-serif; font-style: italic; font-weight: 800; font-size: 23px;
    line-height: 24px; color: var(--white); text-transform: uppercase; letter-spacing: .5px;
  }
  .website {
    position: absolute; left: 762px; top: 94px; width: 320px; height: 24px; background: var(--ink);
    color: var(--white); font-family: "Exo 2", sans-serif; font-weight: 800; font-size: 16px;
    display: flex; align-items: center; justify-content: center;
  }
  .cta { position: absolute; left: 50px; top: 410px; }
  .cta-lead { display: block; color: var(--white); font-size: 27px; line-height: 30px; -webkit-text-stroke: .8px var(--white); }
  .cta-main { display: block; color: var(--accent-yellow); font-size: 35px; line-height: 38px; -webkit-text-stroke: 1.2px var(--accent-yellow); }
  .phone {
    position: absolute; left: 455px; right: 40px; top: 418px; text-align: right;
    color: var(--white); font-size: 54px; line-height: 62px; -webkit-text-stroke: 2px var(--white); letter-spacing: 1px;
  }
</style>
</head>
<body>
<main class="sign">
  <svg class="sign-shapes" viewBox="0 0 1329 611" preserveAspectRatio="none" aria-hidden="false">
    <defs>
      <linearGradient id="sky" x1="0" y1="0" x2="0" y2="1">
        <stop offset="0" stop-color="#1a5fae"/>
        <stop offset=".6" stop-color="#4a90d6"/>
        <stop offset="1" stop-color="#9db4c8"/>
      </linearGradient>
      <linearGradient id="machines" x1="0" y1="0" x2="1" y2="1">
        <stop offset="0" stop-color="#e0a020"/>
        <stop offset=".5" stop-color="#e8b81c"/>
        <stop offset="1" stop-color="#6f6a5e"/>
      </linearGradient>
    </defs>
    <rect class="sky" width="1329" height="611" fill="url(#sky)"/>
    <polygon class="white-panel" points="0,0 558,0 710,115 470,460 0,460" fill="#ffffff"/>
    <polygon class="chevron-blue" points="558,0 650,0 800,115 560,460 470,460 710,115" fill="#1f7fd8"/>
    <polygon class="chevron-silver" points="650,0 700,0 850,115 610,460 560,460 800,115" fill="#cfd6de"/>
    <polygon class="chevron-black" points="700,0 820,0 970,115 730,460 610,460 850,115" fill="#0d0d0d"/>
    <polygon class="chevron-white" points="820,0 840,0 990,115 750,460 730,460 970,115" fill="#ffffff"/>
    <polygon class="equipment-photo" role="img" aria-label="Photo of a yellow wheeled bulldozer, an excavator and trucks lined up on a yard"
      points="520,480 540,330 760,250 1010,170 1329,150 1329,470 1010,500" fill="url(#machines)"/>
    <rect class="bottom-band" x="0" y="460" width="1329" height="151" fill="#1f7fd8"/>
    <polygon class="cta-divider" points="0,460 484,460 514,535 484,611 0,611" fill="#ffffff"/>
    <polygon class="cta-panel" points="0,460 468,460 498,535 468,611 0,611" fill="#0d0d0d"/>
    <polygon class="region-flag" points="0,0 0,0" fill="none"/>
  </svg>

  <div class="brand">
    <span class="brand-square"></span>
    <span class="brand-name">PRAIRIE RIDGE</span>
  </div>

  <h1 class="headline">HEAVY DUTY<br>EQUIPMENT<br>RENTALS</h1>

  <div class="region">
    <span class="region-west" style="background:var(--brand-blue)">WESTERN</span>
    <span class="region-canada" style="background:var(--flag-red);clip-path:polygon(8% 0,100% 0,100% 100%,0 100%)">CANADA</span>
  </div>

  <p class="service"><em>HASSLE-FREE</em> &amp; PERSONALISED SERVICE</p>

  <p class="slogan">Rental Equipments<br>For Your Success</p>
  <p class="website">prairieridgerentals.com</p>

  <p class="cta"><span class="cta-lead">CALL FOR</span><span class="cta-main">ASSISTANCE</span></p>
  <p class="phone">403-555-0148</p>
</main>
</body>
</html>
```